Business Card Design

Contact Information for Business Card

A vertical business card request- a medium & light gray with silverfern tree logo (logo is attached)

Please use Trebuchet font -- if possible- can we use two different color gray? (See pictures attached below)
Info on the front should be the Silverfern tree logo - on the top of the card, followed by the info ...
Card to read: " " indicated what should be on the card --
Name: " Joan Pelley "
Title : "Partner "
" Office: 202.555.0147 "
" Mobile: 202.555.0182 "

Backside of the card - solid medium color gray color w/ address and small message centered in the card - Trebuchet font
to read:

" 317 B North Linden Avenue, NE "
" Washington, DC 20099 "

Then below address to read:
" Fundraising | Event Planning | Political Consulting "

```html
<!DOCTYPE html>
<html lang="en">
<head>
<meta charset="utf-8">
<title>Silverfern Strategies – Business Card</title>
<link rel="stylesheet" href="https://fonts.googleapis.com/css2?family=Fira+Sans:wght@400;500;600&display=swap">
<style>
  :root {
    --canvas: #ffffff;
    --gray-medium: #3d3d3d;
    --gray-light: #b0b0b0;
    --text-dark: #3d3d3d;
    --text-light: #c4c4c4;
    --brand-text: #e6e6e6;
    --shadow: rgba(0, 0, 0, 0.35);
  }
  * { margin: 0; padding: 0; box-sizing: border-box; }
  html, body {
    width: 1200px;
    height: 1200px;
    overflow: hidden;
    background: var(--canvas);
    font-family: "Fira Sans", "Trebuchet MS", sans-serif;
  }
  .canvas { position: relative; width: 1200px; height: 1200px; }

  .card {
    position: absolute;
    top: 221px;
    width: 410px;
    height: 719px;
    background: var(--gray-medium);
    box-shadow: 0 6px 14px var(--shadow);
    overflow: hidden;
  }
  .card--front { left: 173px; }
  .card--back { left: 638px; }

  /* Front */
  .front-brand {
    position: absolute;
    left: 0; top: 0;
    width: 100%;
    height: 414px;
  }
  .brand-name {
    position: absolute;
    right: 18px;
    top: 296px;
    text-align: right;
    color: var(--brand-text);
    font-weight: 400;
    line-height: 1;
  }
  .brand-name .line-main { display: block; font-size: 42px; letter-spacing: 1px; }
  .brand-name .line-sub { display: block; font-size: 22px; letter-spacing: 1.5px; margin-top: 8px; }

  .front-info {
    position: absolute;
    left: 0; top: 414px;
    width: 100%;
    height: 305px;
    background: var(--gray-light);
    color: var(--text-dark);
    padding: 52px 0 0 22px;
  }
  .person-name { font-size: 25px; font-weight: 600; line-height: 1; }
  .person-title { font-size: 22px; font-weight: 400; margin-top: 12px; line-height: 1; }
  .contact-list { list-style: none; margin-top: 55px; font-size: 23px; line-height: 39px; }

  /* Back */
  .back-info {
    position: absolute;
    left: 0; top: 564px;
    width: 100%;
    text-align: center;
    color: var(--text-light);
  }
  .address { font-style: normal; font-size: 21px; font-weight: 500; line-height: 29px; }
  .services { font-size: 14.5px; font-weight: 600; margin-top: 22px; letter-spacing: 0.2px; }
</style>
</head>
<body>
<main class="canvas">
  <section class="card card--front" aria-label="Business card front">
    <div class="front-brand">
      <p class="brand-name">
        <span class="line-main">SILVERFERN</span>
        <span class="line-sub">STRATEGIES</span>
      </p>
    </div>
    <div class="front-info">
      <h1 class="person-name">Joan Pelley</h1>
      <p class="person-title">Partner</p>
      <ul class="contact-list">
        <li>Office: 202.555.0147</li>
        <li>Mobile: 202.555.0182</li>
      </ul>
    </div>
  </section>

  <section class="card card--back" aria-label="Business card back">
    <div class="back-info">
      <address class="address">317 B North Linden Avenue, NE<br>Washington, DC 20099</address>
      <p class="services">Fundraising | Event Planning | Political Consulting</p>
    </div>
  </section>
</main>
</body>
</html>
```